Jumbo Postcard for Pizza Restaurant

i have ordered several thousand postcards already. My postcard has my menu on the back and information about my restaurant on the front. I would like to redesign my existing postcard. The key points of the postcard redesign are as follows.
1. I want to keep the menu on the back but I need to add some menu items and would like the layout to be reformatted so it is easier to read and use. There are also some menu items/descriptions on existing postcard that are too small and don't match the rest of the menu format (specifically: Pastas and Salads)
2. I would like to change the front of the postcard by adding coupons/offers to the customers. I would also like to add new pictures. I will upload pictures and ideas for coupon/offer later this evening. If you wish to proceed before then, perhaps you could just use a space filler until files are received. The overall look of the front of the postcard needs to be changed to reflect the new information and items so our customers take notice it and try new products.
3. The post card needs to be attention-grabbing and new when contrasted and compared to the previous postcard, but I do want it to be clear that it's originating from the same company. Our logo and use of the colors red, black and white should provide some continuity. I am not opposed to adding more color.
4. Just to give you an idea of who we are: We are a family owned and operated restaurant. We offer high quality, fresh ingredients and a premium product for a fair price. We are primarily a delivery and pickup restaurant, but we also have a small dine-in area.
5. When viewing the old postcard (I have uploaded the file) you'll notice an offer to get a second pizza of equal or lesser value for $12. I would like to make this offer more noticeable.
Updates
Project Deadline Extended Reason: I want to extend the deadline for two reasons. 1. I recently had a computer failure that resulted in the loss of some content, including some elements that were to be included in the postcard. I believe I have retrieved the necessary items.2. I am a very busy small business owner and have struggled to find time to work on this postcard and also do everything else required in a day. I appreciate the work, creativity, and submissions of all designers. I am asking for understanding on this matter. It's truly appreciated. Added Tuesday, March 22, 2016
Project Deadline Extended Reason: Need to work out final details. Thanks. Added Friday, April 1, 2016
Target Market(s)
We target families and also have a business lunch crowd.
Industry/Entity Type
Restaurant
Look and feel
Each slider illustrates characteristics of the customer's brand and the style your logo design should communicate.

```html
<!DOCTYPE html>
<html lang="en">
<head>
<meta charset="utf-8">
<title>Harbor Point Pizza Company – Postcard Front</title>
<link rel="stylesheet" href="https://fonts.googleapis.com/css2?family=Oswald:wght@500;700&family=Marcellus&family=Lato:wght@400;700&display=swap">
<style>
  :root {
    --page-bg: #d9d9d9;
    --black: #1d1d1d;
    --black-soft: #2a2a2a;
    --red: #e3202a;
    --red-deep: #a80f16;
    --red-bright: #f0333b;
    --white: #ffffff;
    --silver-light: #f4f4f4;
    --silver-dark: #b9b9b9;
  }
  * { box-sizing: border-box; margin: 0; padding: 0; }
  html, body { width: 1200px; height: 907px; overflow: hidden; }
  body { background: var(--page-bg); position: relative; }

  .postcard {
    position: absolute; left: 20px; top: 133px;
    width: 1160px; height: 640px;
    background: var(--black);
    overflow: hidden;
  }
  .header-band {
    position: absolute; left: 0; top: 0; width: 100%; height: 167px;
    background: linear-gradient(180deg, var(--black-soft), var(--black));
  }
  .brand {
    position: absolute; left: 24px; top: 26px; width: 126px;
    display: flex; flex-direction: column; align-items: center; gap: 8px;
  }
  .brand-dot { width: 46px; height: 46px; border-radius: 50%; background: var(--red); }
  .brand-name {
    font-family: 'Lato', sans-serif; font-weight: 700; font-size: 14px;
    line-height: 1.2; color: var(--white); text-align: center; text-transform: uppercase;
  }
  .headline {
    position: absolute; left: 172px; top: 46px;
    font-family: 'Oswald', sans-serif; font-weight: 500; font-size: 38px;
    line-height: 1; color: var(--red); letter-spacing: -0.4px; text-transform: uppercase;
    white-space: nowrap;
  }
  .subheadline {
    position: absolute; left: 172px; top: 95px;
    font-family: 'Marcellus', serif; font-size: 35px; line-height: 1;
    color: var(--white); letter-spacing: 2.6px; text-transform: uppercase;
    white-space: nowrap;
  }
  .header-rule {
    position: absolute; left: 0; top: 167px; width: 100%; height: 8px; background: var(--white);
  }
  .offer-panel {
    position: absolute; left: 0; top: 175px; width: 100%; height: 396px;
    background: radial-gradient(ellipse at 62% 30%, var(--red-bright) 0%, var(--red) 40%, var(--red-deep) 100%);
  }
  .panel-title {
    position: absolute; left: 34px; top: 205px;
    font-family: 'Marcellus', serif; font-size: 60px; line-height: 1;
    color: var(--white); letter-spacing: 3px; text-transform: uppercase;
    white-space: nowrap;
  }
  .panel-body {
    position: absolute; left: 37px; top: 300px; width: 456px;
    font-family: 'Lato', sans-serif; font-size: 16.4px; line-height: 1.36;
    color: var(--white); text-align: justify; hyphens: auto;
  }
  .photo-frame { position: absolute; left: 0; top: 0; width: 1160px; height: 577px; }
  .footer-rule {
    position: absolute; left: 0; top: 571px; width: 100%; height: 6px; background: var(--white);
  }
  .footer-band {
    position: absolute; left: 0; top: 577px; width: 100%; height: 63px; background: var(--black);
  }
  .website {
    position: absolute; left: 36px; top: 588px;
    font-family: 'Lato', sans-serif; font-size: 30px; line-height: 1;
    color: var(--white); letter-spacing: 21.4px; white-space: nowrap;
  }
  .footer-arrows { position: absolute; left: 1050px; top: 595px; }
  .offer-badge { position: absolute; left: 535px; top: 222px; width: 214px; height: 214px; }
  .offer-text {
    position: absolute; left: 535px; top: 292px; width: 214px;
    font-family: 'Oswald', sans-serif; font-weight: 700; font-size: 31px;
    line-height: 1.15; text-align: center; text-transform: uppercase; white-space: nowrap;
  }
  .offer-text .lead { color: var(--black); display: block; }
  .offer-text .accent { color: var(--red); display: block; }
</style>
</head>
<body>
  <main class="postcard">
    <div class="header-band"></div>
    <div class="brand">
      <span class="brand-dot"></span>
      <span class="brand-name">Harbor Point<br>Pizza Company</span>
    </div>
    <h1 class="headline">Great Pizza Made With Maui’s</h1>
    <p class="subheadline">Freshest Ingredients</p>

    <div class="header-rule"></div>
    <div class="offer-panel"></div>

    <h2 class="panel-title">Lorem Ipsum</h2>
    <p class="panel-body">Lorem Ipsum is simply dummy text of the printing and typesetting industry. Lorem Ipsum has been the industry's standard dummy text ever since the 1500s, when an unknown printer took a galley of type and scrambled it to make a type specimen book. It has survived not only five centuries, but also the leap into electronic typesetting, remaining essentially unchanged. It was popularised in the 1960s with the release of Typeset sheets containing Lorem Ipsum passages, and more recently with desktop publishing software like Pagewright Layout including versions of Lorem Ipsum.</p>

    <svg class="photo-frame" viewBox="0 0 1160 577">
      <defs>
        <radialGradient id="pizzaTone" cx="0.6" cy="0.62" r="0.65">
          <stop offset="0" stop-color="#e9c58a"/>
          <stop offset="0.45" stop-color="#c9552f"/>
          <stop offset="0.8" stop-color="#6b3a22"/>
          <stop offset="1" stop-color="#3a2a22"/>
        </radialGradient>
      </defs>
      <path d="M782,0 Q566,300 712,577" fill="none" stroke="var(--white)" stroke-width="18"/>
      <path d="M774,0 Q558,300 704,577" fill="none" stroke="var(--red)" stroke-width="6"/>
      <path role="img" aria-label="Photo of a pepperoni, sausage and green pepper pizza in a pan with oil and drinks behind it" d="M792,0 Q576,300 722,577 L1160,577 L1160,0 Z" fill="url(#pizzaTone)"/>
    </svg>

    <svg class="offer-badge" viewBox="-100 -100 200 200" aria-hidden="true">
      <defs>
        <radialGradient id="badgeTone" cx="0.4" cy="0.35" r="0.7">
          <stop offset="0" stop-color="var(--silver-light)"/>
          <stop offset="1" stop-color="var(--silver-dark)"/>
        </radialGradient>
      </defs>
      <polygon fill="url(#badgeTone)" points="0,-96 10.4,-79.3 27.3,-92 31,-71.5 51.2,-79.8 47.6,-59.1 69.4,-62.5 58.6,-43.6 80,-39 63.2,-25.5 84.3,-16.4 64.8,-6.2 85.6,5.7 63.6,9.6 79.2,25.2 56.9,26.1 68.6,45.4 48.8,40.7 55.7,62.6 38.2,52.9 39.1,75.4 24.5,62.7 20.2,84.2 8.7,64.9 0,85.7 -8.7,64.9 -20.2,84.2 -24.5,62.7 -39.1,75.4 -38.2,52.9 -55.7,62.6 -48.8,40.7 -68.6,45.4 -56.9,26.1 -79.2,25.2 -63.6,9.6 -85.6,5.7 -64.8,-6.2 -84.3,-16.4 -63.2,-25.5 -80,-39 -58.6,-43.6 -69.4,-62.5 -47.6,-59.1 -51.2,-79.8 -31,-71.5 -27.3,-92 -10.4,-79.3"/>
    </svg>
    <p class="offer-text"><span class="lead">Your</span><span class="accent">Offer Here</span></p>

    <div class="footer-rule"></div>
    <div class="footer-band"></div>
    <p class="website">harborpointpizzacompany.com</p>
    <svg class="footer-arrows" width="52" height="30" viewBox="0 0 52 30" aria-hidden="true">
      <polygon points="16,0 28,0 14,15 28,30 16,30 2,15" fill="var(--red)"/>
      <polygon points="38,0 50,0 36,15 50,30 38,30 24,15" fill="var(--red)"/>
    </svg>
  </main>
</body>
</html>
```